Business Card Design Project for MirelloVantine

Our company needs a Business Card Design. Please refer to our original project in the link above.

Business Card will have the Logo&Symbol withe the Corporate Identity that is beeing created in LayoutNest. Pls see other MirelloVantine Projects.

Target Market(s)

Luxury fashion interested women

Industry/Entity Type

Business

Font styles to use
Other font styles liked:
• Calibri, Arial, Myriad, Helvetica Neue, Lucida Grande, Avenir

```html
<!DOCTYPE html>
<html lang="en">
<head>
<meta charset="utf-8">
<title>MirelloVantine Business Card</title>
<link rel="stylesheet" href="https://fonts.googleapis.com/css2?family=Marcellus&display=swap">
<style>
  :root {
    --navy: #232a6e;
    --gold: #c9a21a;
    --ink: #2b2b33;
    --card: #ffffff;
    --backdrop: #e4e4e6;
  }
  html, body {
    margin: 0;
    padding: 0;
    overflow: hidden;
  }
  .canvas {
    position: relative;
    width: 1200px;
    height: 750px;
    background: var(--backdrop);
    font-family: "Marcellus", serif;
    overflow: hidden;
  }
  .card {
    position: absolute;
    background: var(--card);
  }
  .card--front {
    left: 60px;
    top: 367px;
    width: 540px;
    height: 298px;
    display: flex;
    align-items: center;
    justify-content: center;
  }
  .card--back {
    left: 632px;
    top: 70px;
    width: 510px;
    height: 306px;
  }
  .brand-name {
    color: var(--navy);
    font-weight: 400;
    letter-spacing: 0.18em;
    white-space: nowrap;
  }
  .card--front .brand-name {
    font-size: 30px;
  }
  .card--back .brand-name {
    position: absolute;
    top: 44px;
    left: 0;
    right: 0;
    text-align: center;
    font-size: 22px;
  }
  .person {
    position: absolute;
    top: 156px;
    left: 0;
    right: 0;
    text-align: center;
  }
  .person__name {
    margin: 0;
    color: var(--ink);
    font-size: 19px;
    font-weight: 400;
    letter-spacing: 0.14em;
  }
  .person__title {
    margin: 3px 0 0;
    color: var(--gold);
    font-size: 11px;
  }
  .contacts {
    position: absolute;
    top: 220px;
    list-style: none;
    margin: 0;
    padding: 0;
    color: var(--ink);
    font-size: 13px;
    line-height: 19px;
  }
  .contacts li {
    display: flex;
    align-items: center;
    gap: 10px;
  }
  .contacts--left {
    left: 30px;
  }
  .contacts--right {
    right: 30px;
    text-align: right;
  }
  .contacts--right li {
    justify-content: flex-end;
  }
  .icon {
    width: 12px;
    height: 12px;
    flex: none;
    fill: var(--navy);
  }
</style>
</head>
<body>
<main class="canvas">
  <section class="card card--front" aria-label="Card front">
    <span class="brand-name">MIRELLO VANTINE</span>
  </section>

  <section class="card card--back" aria-label="Card back">
    <div class="brand-name">MIRELLO VANTINE</div>

    <div class="person">
      <h1 class="person__name">ADRIAN MOREL</h1>
      <p class="person__title">Managing Director</p>
    </div>

    <ul class="contacts contacts--left">
      <li>
        <svg class="icon" viewBox="0 0 12 12" aria-hidden="true"><path d="M3 0h6v12H3z M4 1.5v8h4v-8z M5.5 10.2h1v1h-1z" fill-rule="evenodd"/></svg>
        <span>+63 7 2100 5562</span>
      </li>
      <li>
        <svg class="icon" viewBox="0 0 12 12" aria-hidden="true"><path d="M0 4c1-3 11-3 12 0v1.5H9V4H3v1.5H0z M2.5 6h7l1.5 5H1z"/></svg>
        <span>+63 7 2100 5562</span>
      </li>
      <li>
        <svg class="icon" viewBox="0 0 12 12" aria-hidden="true"><path d="M0 2.5h12v7H0z M1 3.5l5 3.5 5-3.5v5.2H1z" fill-rule="evenodd"/></svg>
        <span>adrian@samplehouse.com</span>
      </li>
    </ul>

    <ul class="contacts contacts--right">
      <li>
        <span>123 Name Street</span>
        <svg class="icon" viewBox="0 0 12 12" aria-hidden="true"><path d="M6 0a4.2 4.2 0 0 1 4.2 4.2C10.2 7.5 6 12 6 12S1.8 7.5 1.8 4.2A4.2 4.2 0 0 1 6 0z M6 2.6a1.6 1.6 0 1 0 0 3.2 1.6 1.6 0 0 0 0-3.2z" fill-rule="evenodd"/></svg>
      </li>
      <li>
        <span>Name City, 12345 Name State</span>
        <span class="icon" aria-hidden="true"></span>
      </li>
      <li>
        <span>www.samplehouse.com</span>
        <svg class="icon" viewBox="0 0 12 12" aria-hidden="true"><path d="M6 0a6 6 0 1 1 0 12A6 6 0 0 1 6 0z M6 1.2a4.8 4.8 0 1 0 0 9.6 4.8 4.8 0 0 0 0-9.6z M3.5 3l2.5 1 1 2.5-2 1.5-1-1.5z M7.5 7.5l1.5-.5-.5 2z" fill-rule="evenodd"/></svg>
      </li>
    </ul>
  </section>
</main>
</body>
</html>
```